Website Redesign for Pet Services Facility

We are looking to redesign our current website. The website must be designed in Wix so we can go in and easily edit throughout the life of the website. Design must be professional, simplistic and informative.

Our current website can be found at: www.plumhollowkennels.com

I would like the new site to be on one scrolling page. Sections to include:
Home page
Service teaser: Overnight Care, Grooming, Dog Daycare, Retail
An about us area with text on the left and a video on the right
Testimonial section
Overnight Section
Grooming Section
Dog Daycare Section
Retail
Meet the Team
Contact us: address, phone number, hours, etc.
Newsletter sign up and location map

A second page will be used for reservations and should include fields for.
Name, address, phone number, service: Overnight care, grooming, daycare, Arrival date, departure date, pet name, breed, special requests

Our phone number should be easily found through the pages. 'Request a Reservation' buttons should be found throughout page.

Text from our current site can be uesd as a filler for now as I will go in and finalize text when site is complete. Any photos can be used for now as I will go in and choose final photos as a later date.

I started playing with wix and started with a concept that I can share if you are interested, just let me know.

Industry/Entity Type

Pet

Number of Pages Required

2 page

Font styles to use
Sans Serif

Requirements
Must have
• 'Request a Reservation' Buttons
• Phone number easily visible
• location map
• Hours area
• Newsletter sign up

```html
<!DOCTYPE html>
<html lang="en">
<head>
<meta charset="utf-8">
<title>Plum Hollow Kennels – Pet Services &amp; Dog Walking</title>
<link href="https://fonts.googleapis.com/css2?family=Lato:wght@300;400;700&display=swap" rel="stylesheet">
<style>
:root{
  --green:#93c83e;
  --green-dark:#7cae2c;
  --ink:#333a33;
  --text:#6b6f6b;
  --muted:#9a9e9a;
  --line:#e4e6e2;
  --paper:#ffffff;
  --soft:#f4f6f2;
  --night:#262a27;
  --night-2:#1c1f1d;
}
*{box-sizing:border-box;margin:0;padding:0}
html,body{width:1200px;height:4545px;overflow:hidden}
body{font-family:"Lato",Arial,sans-serif;color:var(--text);background:var(--paper);font-size:14px;line-height:1.6}
a{color:inherit;text-decoration:none}
.wrap{width:1000px;margin:0 auto;position:relative}
.btn{display:inline-block;background:var(--green);color:#fff;font-size:12px;font-weight:700;letter-spacing:.5px;padding:10px 26px;border-radius:20px;text-transform:uppercase}
.section-title{font-weight:300;font-size:40px;color:var(--ink);text-align:center;line-height:1.2}
.section-lead{max-width:640px;margin:14px auto 0;text-align:center;font-size:13px;color:var(--muted)}
.photo{display:block}

/* top bar */
.topbar{height:36px;background:var(--night);color:#c9ccc8;font-size:12px}
.topbar .wrap{display:flex;justify-content:space-between;align-items:center;height:36px}
.topbar .contact{display:flex;gap:22px}
.topbar .contact span{display:flex;align-items:center;gap:6px}

/* header */
.header{height:100px;background:#fff;border-bottom:1px solid var(--line)}
.header .wrap{display:flex;align-items:center;height:100px}
.brand{display:flex;align-items:center;gap:10px;font-weight:700;font-size:20px;color:var(--ink)}
.brand-mark{width:34px;height:34px;background:var(--green);border-radius:4px}
.nav{display:flex;gap:26px;margin-left:auto;margin-right:24px;font-size:14px;color:var(--ink)}
.nav a.active{color:var(--green);border-bottom:2px solid var(--green);padding-bottom:4px}
.call{background:var(--green);color:#fff;font-weight:700;font-size:13px;padding:10px 18px;border-radius:20px}

/* hero */
.hero{height:432px;position:relative;color:#fff;text-align:center}
.hero .photo{position:absolute;inset:0;background:linear-gradient(135deg,#6e8a3c 0%,#a0813f 35%,#6b4a2a 60%,#8fae55 100%)}
.hero-copy{position:relative;padding-top:120px}
.hero h1{font-weight:300;font-size:48px}
.hero p{width:640px;margin:10px auto 26px;font-size:13px;color:#f1f1ea}

/* services */
.services{height:568px;padding-top:64px;background:var(--paper)}
.service-grid{display:flex;gap:28px;margin-top:40px}
.service-card{flex:1;background:#fff;box-shadow:0 2px 10px rgba(0,0,0,.08);text-align:center;padding:26px 20px 24px;border-bottom:3px solid var(--green)}
.service-card .photo{width:116px;height:116px;border-radius:50%;margin:0 auto 16px}
.service-card h3{font-size:17px;color:var(--ink);font-weight:700}
.service-card p{font-size:12px;color:var(--muted);margin:8px 0 14px}
.more{color:var(--green);font-size:12px;font-weight:700}

/* about */
.about{height:364px;display:flex}
.about-copy{width:600px;background:var(--green);color:#fff;padding:60px 60px 0 100px}
.about-copy h2{font-weight:300;font-size:40px;margin-bottom:16px}
.about-copy p{font-size:13px;color:#f3f9ea}
.about .photo{width:600px;background:linear-gradient(120deg,#b8b3a6,#7d7c78 55%,#c48a56)}

/* grooming */
.grooming{height:410px;display:flex;align-items:center}
.grooming .photo{width:520px;height:330px;margin-left:100px;background:radial-gradient(circle at 50% 40%,#2b2b2b 0%,#4a4a4a 40%,#fff 72%)}
.grooming-copy{width:460px;margin-left:40px}
.grooming-copy h2{font-weight:300;font-size:40px;color:var(--ink);margin-bottom:14px}
.grooming-copy p{font-size:13px;color:var(--muted);margin-bottom:22px}

/* overnight / daycare */
.split{height:590px;display:flex}
.split-panel{width:600px;position:relative;padding:60px 70px 0 100px}
.split-panel .photo{position:absolute;inset:0}
.split-panel .inner{position:relative}
.split-panel h2{font-weight:300;font-size:40px;margin-bottom:16px}
.split-panel p{font-size:13px;margin-bottom:24px}
.overnight{color:#fff}
.overnight .photo{background:linear-gradient(160deg,#3d3f3c,#1f211f 70%)}
.overnight p{color:#d5d8d3}
.overnight .btn{background:transparent;border:1px solid #fff}
.daycare{color:var(--ink);padding-left:70px;padding-right:100px}
.daycare .photo{background:linear-gradient(160deg,#f1efe9,#e2d9c9 60%,#efe9dd)}
.daycare p{color:var(--text)}

/* retail */
.retail{height:365px;padding-top:56px}
.brand-row{display:flex;align-items:center;gap:34px;margin-top:40px}
.arrow{width:34px;height:34px;display:flex;align-items:center;justify-content:center;color:var(--ink)}
.partner{flex:1;height:70px;background:var(--soft);border-radius:6px}

/* testimonial */
.testimonial{height:315px;position:relative;text-align:center;color:#fff}
.testimonial .photo{position:absolute;inset:0;background:linear-gradient(90deg,#a9d25d,#c8e39a 50%,#9bc650)}
.testimonial .inner{position:relative;padding-top:46px}
.testimonial h2{font-weight:300;font-size:40px}
.quote{width:620px;margin:16px auto 18px;font-size:13px;font-style:italic;color:#fff}
.avatar{width:56px;height:56px;border-radius:50%;background:#e9d7c1;margin:0 auto;border:3px solid #fff}
.testimonial .author{font-size:12px;margin-top:6px}
.t-arrow{position:absolute;top:150px;width:34px;height:34px;border:1px solid #fff;border-radius:50%;display:flex;align-items:center;justify-content:center}

/* team */
.team{height:435px;padding-top:56px}
.team-row{display:flex;align-items:center;gap:20px;margin-top:40px}
.member{flex:1;display:flex;align-items:center;gap:16px;padding:18px;background:#fff;box-shadow:0 2px 10px rgba(0,0,0,.07)}
.member .photo{width:90px;height:90px;border-radius:50%;background:linear-gradient(135deg,#d9c7b0,#8c7b68)}
.member h4{color:var(--green);font-size:17px}
.member .role{font-size:12px;color:var(--muted)}
.socials{display:flex;gap:6px;margin-top:8px}
.socials span{width:22px;height:22px;border-radius:50%;background:var(--green)}

/* contact */
.contact{height:680px;position:relative;color:#fff}
.contact .photo{position:absolute;inset:0;background:linear-gradient(160deg,#3a3a36,#1b1c1a 70%,#2e2a24)}
.contact .inner{position:relative;padding-top:60px;text-align:center}
.contact h2{font-weight:300;font-size:40px}
.contact .lead{width:620px;margin:12px auto 0;font-size:13px;color:#cfd2cd}
.contact-box{width:920px;height:370px;margin:40px auto 0;background:#fff;display:flex;text-align:left;color:var(--text)}
.map{width:560px;background:linear-gradient(135deg,#eef0ea,#dfe6d6)}
.info{flex:1;padding:30px 34px;font-size:13px}
.info h4{color:var(--ink);font-size:15px;margin-bottom:6px}
.info p{margin-bottom:14px}

/* newsletter */
.newsletter{height:90px;background:var(--green);color:#fff}
.newsletter .wrap{display:flex;align-items:center;height:90px;gap:20px}
.newsletter h3{font-weight:700;font-size:20px}
.field{width:300px;height:38px;background:#fff;border-radius:20px;color:var(--muted);font-size:12px;padding:10px 18px}
.subscribe{background:var(--night);color:#fff;font-size:12px;font-weight:700;padding:11px 22px;border-radius:20px}
.newsletter .socials{margin:0 0 0 auto;gap:10px}
.newsletter .socials span{width:30px;height:30px;background:#fff}

/* footer */
.footer{height:160px;background:var(--night-2);color:#a7aaa5;text-align:center;padding-top:44px;font-size:13px}
.footer nav{display:flex;justify-content:center;gap:30px;color:#e0e2df}
.footer small{display:block;margin-top:22px;font-size:11px}
</style>
</head>
<body>

<div class="topbar">
  <div class="wrap">
    <span>Welcome to Plum Hollow Kennels</span>
    <div class="contact">
      <span><svg width="12" height="12" viewBox="0 0 24 24"><path fill="#93c83e" d="M6.6 10.8a15 15 0 006.6 6.6l2.2-2.2a1 1 0 011-.3 11 11 0 003.6.6 1 1 0 011 1V20a1 1 0 01-1 1A17 17 0 013 4a1 1 0 011-1h3.5a1 1 0 011 1 11 11 0 00.6 3.6 1 1 0 01-.3 1z"/></svg>(555) 014-2280</span>
      <span>Mon–Sat 7:00 – 19:00</span>
    </div>
  </div>
</div>

<header class="header">
  <div class="wrap">
    <a class="brand" href="#"><span class="brand-mark"></span>Plum Hollow</a>
    <nav class="nav">
      <a class="active" href="#">About Us</a><a href="#">Daycare</a><a href="#">Overnight Care</a><a href="#">Grooming</a><a href="#">Shop</a><a href="#">Resources</a><a href="#">Contact Us</a>
    </nav>
    <a class="call" href="#">Call us: (555) 014-2280</a>
  </div>
</header>

<section class="hero">
  <div class="photo" role="img" aria-label="Close-up photo of a dog on green grass"></div>
  <div class="hero-copy">
    <h1>Pet Services &amp; Dog Walking</h1>
    <p>Plum Hollow Kennels offers a caring home away from home for your pet, with spacious play areas, attentive staff and daily walks so every guest returns happy, rested and well looked after.</p>
    <a class="btn" href="#">Request a Reservation</a>
  </div>
</section>

<section class="services">
  <div class="wrap">
    <h2 class="section-title">We Provide Best Services</h2>
    <p class="section-lead">There are many reasons to choose us for your pet's care, from friendly staff to clean spaces and flexible schedules built around your family.</p>
    <div class="service-grid">
      <article class="service-card">
        <div class="photo" role="img" aria-label="Dog resting for overnight care" style="background:linear-gradient(135deg,#c9b79c,#7d6a55)"></div>
        <h3>Overnight Care</h3><p>Leaving your pet overnight should not be a worry for either of you.</p><a class="more" href="#">Learn more ›</a>
      </article>
      <article class="service-card">
        <div class="photo" role="img" aria-label="Dog being groomed" style="background:linear-gradient(135deg,#e6ddd0,#a48f77)"></div>
        <h3>Grooming</h3><p>Grooming at Plum Hollow is done by our skilled team.</p><a class="more" href="#">Learn more ›</a>
      </article>
      <article class="service-card">
        <div class="photo" role="img" aria-label="Dogs playing at daycare" style="background:linear-gradient(135deg,#a6c46c,#6b7d49)"></div>
        <h3>Dog Daycare</h3><p>Socialization is one of the most important parts of canine life.</p><a class="more" href="#">Learn more ›</a>
      </article>
      <article class="service-card">
        <div class="photo" role="img" aria-label="Pet food retail shelves" style="background:linear-gradient(135deg,#d7c5a8,#8a6e4e)"></div>
        <h3>Retail</h3><p>As part of our dedication to the health of pets, we offer quality food.</p><a class="more" href="#">Learn more ›</a>
      </article>
    </div>
  </div>
</section>

<section class="about">
  <div class="about-copy">
    <h2>About Us</h2>
    <p>Since opening our doors we have cared for thousands of dogs and cats in a calm, clean and friendly setting. Our team is trained in pet first aid and loves every guest. We welcome visitors to tour the facility at any time and meet the people who will care for your pet.</p>
  </div>
  <div class="photo" role="img" aria-label="Video still of a grey dog playing with a rope toy"></div>
</section>

<section class="grooming">
  <div class="photo" role="img" aria-label="Illustration of a groomed dog with curly hair and sunglasses, surrounded by grooming tools"></div>
  <div class="grooming-copy">
    <h2>Grooming</h2>
    <p>Grooming at Plum Hollow is done by our skilled staff. From gentle baths to full breed trims, we take time to keep your pet calm and looking great. Book a grooming visit on its own or add it to any stay with us.</p>
    <a class="btn" href="#">Learn more</a>
  </div>
</section>

<section class="split">
  <div class="split-panel overnight">
    <div class="photo" role="img" aria-label="Dark photo of a dog resting at night"></div>
    <div class="inner">
      <h2>Overnight Care</h2>
      <p>Leaving your pet overnight should not be a stressful time for either of you. Your pet will enjoy a comfortable suite, regular walks, playtime and a quiet evening routine. Please speak with us about feeding, medication and any special needs so we can prepare before arrival.</p>
      <a class="btn" href="#">Learn more</a>
    </div>
  </div>
  <div class="split-panel daycare">
    <div class="photo" role="img" aria-label="Light photo of a dog at daycare"></div>
    <div class="inner">
      <h2>Dog Daycare</h2>
      <p>Socialization is one of the most important parts of a dog's life. Our daycare groups are matched by size and energy, supervised all day, and include rest breaks. It is a great choice for busy days at work.</p>
      <a class="btn" href="#">Learn more</a>
    </div>
  </div>
</section>

<section class="retail">
  <div class="wrap">
    <h2 class="section-title">The Plum Hollow Retail</h2>
    <p class="section-lead">As part of our dedication to the health of pets, we stock a selection of trusted foods, treats and supplies.</p>
    <div class="brand-row">
      <span class="arrow"><svg width="12" height="20" viewBox="0 0 12 20"><path d="M10 2L2 10l8 8" fill="none" stroke="#333a33" stroke-width="2"/></svg></span>
      <span class="partner"></span><span class="partner"></span><span class="partner"></span><span class="partner"></span><span class="partner"></span>
      <span class="arrow"><svg width="12" height="20" viewBox="0 0 12 20"><path d="M2 2l8 8-8 8" fill="none" stroke="#333a33" stroke-width="2"/></svg></span>
    </div>
  </div>
</section>

<section class="testimonial">
  <div class="photo" role="img" aria-label="Green-tinted photo of a pet owner with a dog"></div>
  <div class="inner">
    <h2>They Say About Us</h2>
    <p class="quote">“Our dog could not wait to get out of the car every visit. The staff are kind, the place is spotless and we always get updates. We would not trust anyone else.”</p>
    <div class="avatar" role="img" aria-label="Customer portrait"></div>
    <p class="author">Happy Client</p>
  </div>
  <span class="t-arrow" style="left:120px"><svg width="8" height="14" viewBox="0 0 8 14"><path d="M7 1L1 7l6 6" fill="none" stroke="#fff" stroke-width="2"/></svg></span>
  <span class="t-arrow" style="right:120px"><svg width="8" height="14" viewBox="0 0 8 14"><path d="M1 1l6 6-6 6" fill="none" stroke="#fff" stroke-width="2"/></svg></span>
</section>

<section class="team">
  <div class="wrap">
    <h2 class="section-title">Meet Our Team</h2>
    <p class="section-lead">Our friendly team is made up of caring people who treat every pet like their own.</p>
    <div class="team-row">
      <span class="arrow"><svg width="12" height="20" viewBox="0 0 12 20"><path d="M10 2L2 10l8 8" fill="none" stroke="#333a33" stroke-width="2"/></svg></span>
      <div class="member"><div class="photo" role="img" aria-label="Team member portrait with a dog"></div><div><h4>John Smith</h4><p class="role">Pet Care</p><div class="socials"><span></span><span></span><span></span></div></div></div>
      <div class="member"><div class="photo" role="img" aria-label="Team member portrait with a dog"></div><div><h4>John Smith</h4><p class="role">Groomer</p><div class="socials"><span></span><span></span><span></span></div></div></div>
      <div class="member"><div class="photo" role="img" aria-label="Team member portrait with a dog"></div><div><h4>John Smith</h4><p class="role">Manager</p><div class="socials"><span></span><span></span><span></span></div></div></div>
      <span class="arrow"><svg width="12" height="20" viewBox="0 0 12 20"><path d="M2 2l8 8-8 8" fill="none" stroke="#333a33" stroke-width="2"/></svg></span>
    </div>
  </div>
</section>

<section class="contact">
  <div class="photo" role="img" aria-label="Dark photo of a dog lying on a wooden floor"></div>
  <div class="inner">
    <h2>Contact Us</h2>
    <p class="lead">Please call or email to book a stay or arrange a tour. We look forward to meeting you and your pet.</p>
    <div class="contact-box">
      <div class="map" role="img" aria-label="Location map of the facility"></div>
      <div class="info">
        <h4>Address</h4>
        <p>418 Orchard Lane, Millbrook</p>
        <h4>Phone</h4>
        <p>(555) 014-2280<br>hello@plumhollowkennels.com</p>
        <h4>Hours</h4>
        <p>Mon–Fri 7:00 – 19:00<br>Sat 8:00 – 17:00<br>Closed Sundays and holidays</p>
        <a class="btn" href="#">Request a Reservation</a>
      </div>
    </div>
  </div>
</section>

<section class="newsletter">
  <div class="wrap">
    <h3>Newsletter Sign Up:</h3>
    <span class="field">Your email address</span>
    <a class="subscribe" href="#">Subscribe</a>
    <div class="socials"><span></span><span></span><span></span><span></span></div>
  </div>
</section>

<footer class="footer">
  <nav><a href="#">About Us</a><a href="#">Daycare</a><a href="#">Overnight Care</a><a href="#">Grooming</a><a href="#">Shop</a><a href="#">Resources</a><a href="#">Contact Us</a></nav>
  <small>© Plum Hollow Kennels · www.plumhollowkennels.com · All rights reserved</small>
</footer>

</body>
</html>
```